Nimbo58.com.au Website and company image design

We are looking for an exceptional website designer / company to work with our new Australian Hosting Company

Nimbo58 is a new Cloud Hosting company launching in Australia that provides Scalable, On Demand computing resources to the Australian Market Place. Scalable, On Demand ocmputing is a nice way of saying fully scalable / redundant Virtual Private Server.

We require a full company image to be developed along with a Logo and Website. There is scope for ongoing development (preferred) for the successful candidate.

Website developement will require extensive jQuery ability (sliders for ordering etc (see: http://www.hostrix-example.com.au/virtual-dedicated-servers/253/zar_vps.html).

Please communicate directly with me to establish full website scope and request further documentation / content.

Target Market(s)

Website Designers, programmers, technicians and large companies

Industry/Entity Type

It Company

Requirements
Must have
• Slider ordering system such as http://www.hostrix-example.com.au/virtual-dedicated-servers/253/zar_vps.html

Nice to have
• CMS backend system
Should not have
• Should NOT be a monster template copy!!!

```html
<!DOCTYPE html>
<html lang="en">
<head>
<meta charset="utf-8">
<title>Nimbo58 – Cloud Hosting</title>
<link href="https://fonts.googleapis.com/css2?family=Roboto+Condensed:wght@400;700&family=Arimo:wght@400;700&display=swap" rel="stylesheet">
<style>
:root{
  --blue:#1fb4e6;
  --blue-dark:#0f8fc0;
  --green:#6aa81c;
  --green-light:#8cc63f;
  --nav:#2a2a2a;
  --ink:#333;
  --muted:#666;
  --panel:#ebebeb;
  --line:#d6d6d6;
  --footer:#3b3b3b;
  --footer-col:#444;
  --footer-text:#c9c9c9;
  --white:#fff;
}
*{box-sizing:border-box;margin:0;padding:0}
html,body{width:689px;height:1200px;overflow:hidden}
body{position:relative;background:var(--white);font-family:"Arimo",Arial,sans-serif;color:var(--ink);font-size:8px}
.abs{position:absolute}
.cond{font-family:"Roboto Condensed","Arial Narrow",sans-serif}
ul{list-style:none}

/* top nav */
.topnav{left:0;top:0;width:689px;height:26px;background:var(--nav);display:flex;justify-content:center}
.topnav a{color:#fff;text-decoration:none;font-family:"Roboto Condensed",sans-serif;font-size:10px;padding:0 13px;line-height:26px;border-right:1px solid #444}
.topnav a:last-child{border-right:0}

/* header */
.header{left:0;top:26px;width:689px;height:56px;background:var(--blue)}
.brand{left:34px;top:12px;color:#fff;font-family:"Arimo",sans-serif;font-weight:700;font-size:25px}
.login input{position:absolute;top:9px;height:15px;border:0;font-size:8px;padding-left:4px;background:#fff}
.signin{left:620px;top:9px;width:35px;height:15px;background:#111;color:#fff;font-size:8px;text-align:center;line-height:15px}
.meta{left:482px;top:35px;color:#fff;font-size:8px}
.region{left:620px;top:33px;width:35px;height:13px;background:#fff;color:#333;font-size:8px;padding-left:3px;line-height:13px}

/* hero */
.hero{left:0;top:82px;width:689px;height:208px;background:linear-gradient(#f4f4f4,#e2e2e2)}
.hero-img{left:62px;top:40px;width:136px;height:158px;border-radius:10px;background:radial-gradient(circle at 50% 45%,#6a6a6a,#2b2b2b 70%,#dcdcdc 72%)}
.hero h1{left:220px;top:18px;font-family:"Roboto Condensed",sans-serif;font-size:21px;font-weight:700;color:#222}
.hero h1 b{font-size:28px}
.hero-list{left:230px;top:62px;font-size:10px;color:#333}
.hero-list li{height:15px;display:flex;align-items:center;gap:5px}
.dot-tick{width:9px;height:9px;border-radius:50%;background:var(--green)}
.btn{position:absolute;font-size:8px;font-weight:700;text-align:center;line-height:21px;height:22px;border-radius:2px}
.btn-blue{background:var(--blue);color:#123}
.btn-green{background:var(--green-light);color:#223}
.arrow{top:68px}
.vps-card{left:497px;top:60px;width:142px;height:116px;background:#fff;border:1px solid #cfe9f5}
.vps-card h3{position:absolute;left:9px;top:8px;color:var(--blue-dark);font-family:"Roboto Condensed",sans-serif;font-size:11px;line-height:12px;font-weight:700}
.vps-card ul{position:absolute;left:9px;top:37px;font-size:7px;line-height:11px}
.price-badge{left:97px;top:6px;width:40px;height:40px;border-radius:50%;background:#fff;border:2px solid #bfe6f6;text-align:center;color:var(--green);font-weight:700}
.vps-cta{left:21px;top:90px;width:100px;height:16px;background:var(--blue);color:#123;font-size:8px;line-height:16px;padding-left:5px}
.dots{left:307px;top:193px;display:flex;gap:3px}
.dots span{width:8px;height:8px;border-radius:50%;background:#bbb}
.dots span:first-child{background:var(--blue)}

/* main */
.h2{font-family:"Roboto Condensed",sans-serif;font-weight:700;font-size:12px}
.h2.dark{color:#333}
.h2.blue{color:var(--blue-dark)}
.rule{height:1px;background:var(--blue)}
.copy{font-size:7px;line-height:10px;color:#555;width:485px}

.config{left:33px;top:380px;width:487px;height:268px;background:var(--panel)}
.config .lbl{position:absolute;left:10px;font-weight:700;font-size:9px;color:#333}
.os-select{left:10px;top:26px;width:331px;height:17px;background:#fff;border:1px solid #ccc;font-size:7px;line-height:15px;padding-left:5px}
.slider-label{position:absolute;left:10px;width:466px;font-size:7px;display:flex;justify-content:space-between}
.slider-label b{font-weight:700}
.track{position:absolute;left:10px;width:466px;height:8px;border-radius:4px;background:#555}
.track i{position:absolute;left:1px;top:1px;height:6px;border-radius:3px;background:var(--green-light)}
.knob{position:absolute;top:-4px;width:14px;height:14px;border-radius:50%;background:radial-gradient(#fff,#bbb);border:1px solid #999}
.price-box{left:260px;top:238px;width:133px;height:20px;background:#fff;border:1px solid #ccc;font-size:8px;font-weight:700;line-height:18px;padding-left:7px}
.select-sw{left:396px;top:238px;width:80px;height:20px;background:var(--green-light);font-size:8px;font-weight:700;line-height:20px;text-align:center}

.tabs{left:43px;top:722px;display:flex;gap:4px}
.tabs span{height:18px;line-height:18px;padding:0 9px;font-size:8px;font-weight:700}
.tab-on{background:var(--blue)}
.tab-off{background:#444;color:#fff}
.perf{left:33px;top:740px;width:487px;border-collapse:collapse;font-size:7px}
.perf td,.perf th{height:25px;border-bottom:1px solid #fff}
.perf td:first-child{padding-left:10px;background:#fff;border-bottom:1px solid #eee}
.perf th{background:#ccc;font-weight:700;height:17px}
.perf td.c{text-align:center;background:#e6e6e6;width:102px}
.perf .gap{width:5px;background:#fff!important;padding:0}

/* sidebar */
.side{left:533px;width:122px;background:#fff;border:1px solid #ddd;box-shadow:0 1px 2px rgba(0,0,0,.15)}
.side-h{height:20px;background:var(--blue);color:#fff;font-family:"Roboto Condensed",sans-serif;font-weight:700;font-size:10px;line-height:20px;padding-left:7px}
.side ul{padding:8px 0 0 9px;font-size:7px;line-height:13px}
.side ul li::before{content:"» ";color:#555}
.side .big{color:var(--green);font-family:"Roboto Condensed",sans-serif;font-size:18px;font-weight:700;padding:6px 0 0 7px}
.side .big small{font-size:8px}
.side .feat{font-size:7px;line-height:11px;padding:2px 0 0 7px}
.corner{position:absolute;right:0;bottom:0;width:0;height:0;border-left:22px solid transparent;border-bottom:22px solid var(--green)}
.dom-in{left:8px;top:30px;width:46px;height:15px;border:1px solid #ccc}
.dom-sel{left:58px;top:30px;width:56px;height:15px;border:1px solid #ccc;font-size:7px;line-height:13px;padding-left:3px}
.dom-btn{left:21px;top:53px;width:78px;height:15px;background:var(--green-light);font-size:7px;line-height:15px;text-align:center}
.feat-btn{position:absolute;left:533px;width:122px;height:22px;background:linear-gradient(#f7f7f7,#e3e3e3);border:1px solid #ccc;font-size:8px;font-weight:700;line-height:20px;padding-left:9px;display:flex;align-items:center;gap:6px}
.feat-btn i{width:9px;height:9px;background:#555;border-radius:2px}

/* partners */
.partners{left:33px;top:880px;width:622px;height:52px;background:#fff;box-shadow:0 2px 6px rgba(0,0,0,.15);display:flex;justify-content:space-around;align-items:center}
.partners span{background:#cfcfcf}

/* footer */
.footer{left:0;top:944px;width:689px;height:226px;background:var(--footer)}
.fcol{position:absolute;top:0;width:148px;height:226px}
.fcol h4{position:absolute;left:18px;top:17px;color:var(--blue);font-family:"Roboto Condensed",sans-serif;font-size:11px;display:flex;gap:5px;align-items:center}
.fcol h4 i{width:11px;height:11px;border-radius:50%;background:var(--blue)}
.fcol ul{position:absolute;left:18px;top:35px;font-size:7px;line-height:13px;color:var(--footer-text)}
.fcol li::before{content:"» ";color:#999}
.bottom{left:33px;top:1180px;font-size:7px;color:#333}
.social{left:572px;top:1176px;display:flex;gap:4px}
.social span{width:17px;height:17px;border-radius:3px;background:#8a8a8a}
</style>
</head>
<body>

<nav class="abs topnav">
  <a>Home</a><a>Domains</a><a>Web Hosting</a><a>Virtual Servers</a><a>Dedicated Servers</a><a>Resellers</a><a>About Us</a><a>Support</a>
</nav>

<header class="abs header">
  <div class="abs brand">Nimbo58</div>
  <div class="login">
    <input style="left:442px;width:84px" value="Email">
    <input style="left:531px;width:84px" value="Password">
  </div>
  <div class="abs signin">Sign in</div>
  <div class="abs meta">Register &nbsp;/&nbsp; Contact us &nbsp;/&nbsp; 111-555-0199</div>
  <div class="abs region">NSW ▾</div>
</header>

<section class="abs hero">
  <svg class="abs arrow" style="left:4px" width="32" height="74" viewBox="0 0 32 74"><path d="M30 2 4 37l26 35" fill="none" stroke="#bdbdbd" stroke-width="6"/></svg>
  <svg class="abs arrow" style="left:654px" width="32" height="74" viewBox="0 0 32 74"><path d="M2 2l26 35L2 72" fill="none" stroke="#bdbdbd" stroke-width="6"/></svg>
  <div class="abs hero-img" role="img" aria-label="Product photo of a server tower on wheels"></div>
  <h1 class="abs">Professional Web Hosting from <b>$9.90</b></h1>
  <ul class="abs hero-list">
    <li><span class="dot-tick"></span>Unlimited Hosting Space</li>
    <li><span class="dot-tick"></span>Unlimited Monthly Bandwidth</li>
    <li><span class="dot-tick"></span>Host Unlimited Domains</li>
    <li><span class="dot-tick"></span>Free Domain Host for Life</li>
  </ul>
  <div class="btn btn-blue" style="left:233px;top:138px;width:61px">Read More</div>
  <div class="btn btn-green" style="left:304px;top:138px;width:63px">Order Now!</div>
  <div class="abs vps-card">
    <h3>Virtual Private<br>SERVER</h3>
    <div class="abs price-badge"><span style="font-size:8px;vertical-align:top">$</span><span style="font-size:18px">12</span><div style="font-size:8px;margin-top:-4px">.95</div></div>
    <ul>
      <li>→ Root VPS Access</li>
      <li>→ 96 - 1GB memory</li>
      <li>→ 4GB - 16GB of Disk</li>
      <li>→ 30 - 200GB Data Transfer</li>
    </ul>
    <div class="abs vps-cta">Click here to Order ✓</div>
  </div>
  <div class="abs dots"><span></span><span></span><span></span><span></span><span></span></div>
</section>

<main>
  <div class="abs h2 dark" style="left:33px;top:299px">ZarServer VDS</div>
  <div class="abs rule" style="left:33px;top:318px;width:107px"></div>
  <p class="abs copy" style="left:33px;top:324px">Lorem Ipsum is simply dummy text of the printing and typesetting industry. Lorem Ipsum has been the industry's standard dummy text ever since the 1500s, when an unknown printer took a galley of type and scrambled it to make a type specimen book. It has survived not only five centuries, but also the leap into electronic typesetting, remaining essentially unchanged.</p>
  <div class="abs h2 blue" style="left:33px;top:362px">Build Your Server</div>

  <section class="abs config">
    <div class="lbl" style="top:9px">Select your Operating System</div>
    <div class="abs os-select">Winforge Server 2003 R2 (32-bit) - ($15.95 per month)<span style="position:absolute;right:5px">▾</span></div>
    <div class="lbl" style="top:55px">Customise your System</div>

    <div class="slider-label" style="top:73px"><span><b>CPU cores</b> ($15.00 per Core)</span><b>2 Cores</b></div>
    <div class="track" style="top:87px"><i style="width:97px"></i><span class="knob" style="left:90px"></span></div>

    <div class="slider-label" style="top:106px"><span><b>Disk Space</b> ($0.59 per GB)</span><b>31 GB</b></div>
    <div class="track" style="top:121px"><i style="width:123px"></i><span class="knob" style="left:116px"></span></div>

    <div class="slider-label" style="top:140px"><span><b>Dedicated RAM</b> ($15.00 per GB)</span><b>5 GB</b></div>
    <div class="track" style="top:154px"><i style="width:147px"></i><span class="knob" style="left:140px"></span></div>

    <div class="slider-label" style="top:173px"><span><b>Premium Bandwidth</b> ($0.70 per GB)</span><b>45 GB</b></div>
    <div class="track" style="top:188px"><i style="width:97px"></i><span class="knob" style="left:90px"></span></div>

    <div class="slider-label" style="top:206px"><span><b>IP Addresses</b> ($3.50 per IP Address)</span><b>1 IP</b></div>
    <div class="track" style="top:220px"><i style="width:110px"></i><span class="knob" style="left:103px"></span></div>

    <div class="abs price-box">Monthly Price: $61.15</div>
    <div class="abs select-sw">Select Software</div>
  </section>

  <div class="abs h2 blue" style="left:33px;top:659px">Speed &amp; Performance</div>
  <div class="abs rule" style="left:33px;top:677px;width:135px"></div>
  <p class="abs copy" style="left:33px;top:683px">Lorem Ipsum is simply dummy text of the printing and typesetting industry. Lorem Ipsum has been the industry's standard dummy text ever since the 1500s, when an unknown printer took a galley of type and scrambled it to make a type specimen book. It has survived not only five centuries, but also the leap into electronic typesetting, remaining essentially unchanged.</p>

  <div class="abs tabs"><span class="tab-on">Test 1</span><span class="tab-off">Test 2</span></div>
  <table class="abs perf">
    <tr><th style="background:#fff"></th><th>Zar Server</th><th class="gap"></th><th>VirtuMax</th></tr>
    <tr><td>Number of workload virtual machines</td><td class="c">6</td><td class="gap"></td><td class="c">6</td></tr>
    <tr><td>Number of database virtual machines</td><td class="c">1</td><td class="gap"></td><td class="c">1</td></tr>
    <tr><td>Average CPU operations per VM</td><td class="c">36.5 Billion per hour</td><td class="gap"></td><td class="c">29.5 Billion per hour</td></tr>
    <tr><td>Average RAM operations per VM</td><td class="c">112 Billion per hour</td><td class="gap"></td><td class="c">88.5 Billion per hour</td></tr>
    <tr><td>Average SQL job completion time</td><td class="c">4 minutes 26 seconds</td><td class="gap"></td><td class="c">5 minutes 8 seconds</td></tr>
  </table>
</main>

<aside>
  <div class="abs side" style="top:304px;height:111px">
    <div class="side-h">Cloud VPS</div>
    <ul><li>Zar VPS</li><li>Hypervane VPS</li><li>VirtuMax VPS</li><li>VDS Backup</li><li>Zar VPS</li><li>Hypervane VPS</li></ul>
  </div>
  <div class="abs side" style="top:427px;height:80px">
    <div class="side-h">Domain Search</div>
    <div class="abs dom-in"></div>
    <div class="abs dom-sel">.com.au ▾</div>
    <div class="abs dom-btn">Check your Domain</div>
  </div>
  <div class="abs side" style="top:517px;height:92px">
    <div class="side-h">Dedicated Server</div>
    <div class="big">$49.95 <small>P/Month</small></div>
    <div class="feat">Unlimited bandwidth<br>Temote Serverr Control<br>Secure Private Network</div>
    <span class="corner"></span>
  </div>
  <div class="abs side" style="top:620px;height:92px">
    <div class="side-h">Broadband</div>
    <div class="big">$35.95 <small>P/Month</small></div>
    <div class="feat">New Domain Privacy<br>Bulk-Buy Discount<br>Advanced DNS Control</div>
    <span class="corner"></span>
  </div>
  <div class="abs side" style="top:722px;height:20px;border:0"><div class="side-h">Cloud Server Features</div></div>
  <div class="feat-btn" style="top:746px"><i></i>Instantly Scale</div>
  <div class="feat-btn" style="top:771px"><i></i>Flexible Pricing</div>
  <div class="feat-btn" style="top:796px"><i></i>Community Support</div>
  <div class="feat-btn" style="top:821px"><i></i>Free Monitoring</div>
  <div class="feat-btn" style="top:846px"><i></i>DNS Management</div>
</aside>

<div class="abs partners" aria-label="Partner badges">
  <span style="width:58px;height:18px"></span>
  <span style="width:38px;height:20px"></span>
  <span style="width:92px;height:16px"></span>
  <span style="width:52px;height:36px;background:#555"></span>
  <span style="width:50px;height:28px;border-radius:50%"></span>
  <span style="width:70px;height:20px"></span>
</div>

<footer class="abs footer">
  <div class="fcol" style="left:22px">
    <h4><i></i>Web Hosting</h4>
    <ul><li>Winforge or Tuxen?</li><li>Tuxen Hosting</li><li>Winforge Hosting</li><li>SSL Certificates</li><li>Advanced WebMail</li><li>Active Spam Filtering</li><li>Hosting Control Panel</li><li>Application Vault</li></ul>
  </div>
  <div class="fcol" style="left:177px">
    <h4><i></i>VPS Virtual Servers</h4>
    <ul><li>Tuxen VPS</li><li>Winforge VPS</li><li>Winforge Pleskor VPS</li><li>Tuxen Pleskor VPS</li><li>Pleskor Hosting VPS</li><li>cPlane Virtual Servers</li><li>Fantasio Add-on</li><li>cPlane VPS</li><li>Zar VPS</li><li>Hypervane VPS</li><li>VirtuMax VPS</li><li>VDS Backup</li><li>Cloud VPS</li><li>Forex VPS</li></ul>
  </div>
  <div class="fcol" style="left:332px">
    <h4><i></i>Dedicated Servers</h4>
    <ul><li>Special Offers</li><li>Same-Day Dedicated</li><li>Small Business Servers</li><li>Medium Business Servers</li><li>Enterprise Servers</li><li>Winforge Dedicated Servers</li><li>Backup and Recovery</li><li>Data Center</li><li>Remote Access / Reboot</li><li>Dedicated Server FAQ</li><li>Request a Quote</li></ul>
  </div>
  <div class="fcol" style="left:485px">
    <h4><i></i>About Nimbo58</h4>
    <ul><li>About Hostrix</li><li>Partners</li><li>Terms of Service</li><li>Service Level Agreement</li><li>Privacy Policy</li><li>Refund Policy</li><li>Jobs @ Hostrix</li><li>Contact Us</li></ul>
  </div>
</footer>

<div class="abs bottom">Copyright © &nbsp;2012-2013 Nimbo58. All Rights Reserved &nbsp;| &nbsp;Privacy &nbsp;| Sitmap</div>
<div class="abs social" aria-label="Social links"><span></span><span></span><span></span><span></span></div>

</body>
</html>
```